Product Insert / Thank You

I'm looking for a small card to be designed that will be included with our product when it ships. It will be 2 sided with 1 side being a "thank you" with our logo and the other side containing the following text:We would love to hear your feedback! For every review we receive on our products, we donate 100% of the proceeds of your order to TIDEWELL -- a non profit organization dedicated to preserving our oceans!If you are not 100% satisfied with your purchase or have any problems, we will always resolve your issue. please contact us via Brisko if you need assistance.Insert needs to be well organized and information presented in a clear and visually appealing way.
Target Market(s)
Women, aged 24-45
Colors
Designer to choose colors to be used in the design.
Look and feel
Each slider illustrates characteristics of the customer's brand and the style your logo design should communicate.

```html
<!DOCTYPE html>
<html lang="en">
<head>
<meta charset="utf-8">
<title>Thank You Insert Card – NORTHPEAK</title>
<link rel="stylesheet" href="https://fonts.googleapis.com/css2?family=Cabin:wght@400;500&display=swap">
<style>
  :root {
    --backdrop: #3a3b3d;
    --card-black: #151515;
    --card-black-edge: #0b0b0b;
    --card-white: #ffffff;
    --ink: #141414;
    --gold: #f2c21b;
    --gold-deep: #d9a40c;
    --emboss: #2a2a2a;
    --emboss-line: #3a3a3a;
  }
  * { box-sizing: border-box; margin: 0; padding: 0; }
  html, body {
    width: 1200px;
    height: 900px;
    overflow: hidden;
  }
  body {
    background: var(--backdrop);
    font-family: "Cabin", "Gill Sans", sans-serif;
    display: flex;
    align-items: center;
    justify-content: center;
    gap: 60px;
  }
  .card {
    width: 525px;
    height: 300px;
    border-radius: 26px;
    position: relative;
    box-shadow: 0 18px 40px rgba(0, 0, 0, 0.45);
  }
  .card--front {
    background: linear-gradient(160deg, #222 0%, var(--card-black) 55%, var(--card-black-edge) 100%);
    display: flex;
    flex-direction: column;
    align-items: center;
    justify-content: center;
    gap: 46px;
  }
  .brand-mark {
    display: flex;
    align-items: center;
    gap: 12px;
    color: var(--emboss-line);
    font-size: 20px;
    font-weight: 500;
    letter-spacing: 2px;
  }
  .brand-mark__dot {
    width: 22px;
    height: 22px;
    border-radius: 50%;
    border: 2px solid var(--emboss-line);
    background: var(--emboss);
  }
  .thank-you {
    font-size: 46px;
    font-weight: 400;
    letter-spacing: -1px;
    background: linear-gradient(180deg, var(--gold) 0%, var(--gold-deep) 100%);
    -webkit-background-clip: text;
    background-clip: text;
    color: transparent;
  }
  .card--back {
    background: var(--card-white);
    display: flex;
    align-items: center;
    justify-content: center;
    padding: 0 34px;
  }
  .insert-copy {
    color: var(--ink);
    font-size: 15.5px;
    line-height: 1.25;
    text-align: center;
  }
  .insert-copy p + p { margin-top: 2px; }
</style>
</head>
<body>
  <section class="card card--front" aria-label="Front of insert card">
    <div class="brand-mark">
      <span class="brand-mark__dot"></span>
      <span class="brand-mark__name">NORTHPEAK</span>
    </div>
    <h1 class="thank-you">THANK YOU</h1>
  </section>

  <section class="card card--back" aria-label="Back of insert card">
    <div class="insert-copy">
      <p>We would love to hear your feedback! For every review we receive on our products, We donate 100% of the proceeds of your order to TIDEWELL -- a non profit organization dedicated to preserving our oceans!</p>
      <p>If you are not 100% satisfied with your purchase or have any problems, we will always resolve your issue. please contact us via Brisko if you need assistance. Insert needs to be well organized and information presented in a clear and visually appealing way</p>
    </div>
  </section>
</body>
</html>
```